Sleek, Professional Business Card Design Needed

Business Cards - Logo Attached.

We are a solar consulting company. We are national and want our cards to represent the professional high quality products that we offer.

Industry/Entity Type

Business

Contact Information for Business Card

n/a

Requirements
Must have
• Design
• Name
• Position
• Number
• Email
• Address
Should not have
• Not be too crowded

```html
<!DOCTYPE html>
<html lang="en">
<head>
<meta charset="utf-8">
<title>Sun Harbor Energy – Business Card</title>
<link rel="stylesheet" href="https://fonts.googleapis.com/css2?family=Open+Sans:wght@400;600;700&display=swap">
<style>
  :root {
    --backdrop: #3b3531;
    --card: #1c1d1f;
    --card-edge: #111213;
    --brand-blue: #1f95d6;
    --brand-green: #7dba2f;
    --text-light: #f1f1f1;
    --text-muted: #9a9a9a;
    --divider: #d8d8d8;
  }
  * { margin: 0; padding: 0; box-sizing: border-box; }
  html, body {
    width: 1200px; height: 864px; overflow: hidden;
    background: var(--backdrop);
    font-family: "Open Sans", Arial, sans-serif;
  }
  .stage { position: relative; width: 1200px; height: 864px; }
  .card {
    position: absolute;
    width: 525px; height: 300px;
    background: var(--card);
    border-radius: 4px;
    box-shadow: 0 14px 30px rgba(0,0,0,.45), 0 0 0 1px var(--card-edge);
  }
  .card--front { left: 55px; top: 90px; }
  .card--back { left: 620px; top: 470px; }

  .brand-block {
    position: absolute;
    display: flex; flex-direction: column; align-items: center;
  }
  .brand__dot {
    width: 54px; height: 54px; border-radius: 50%;
    border: 5px solid var(--brand-blue);
    margin-bottom: 8px;
  }
  .brand__name {
    color: var(--brand-blue);
    font-weight: 700; font-size: 24px; letter-spacing: .5px;
    white-space: nowrap;
  }
  .brand__rule { align-self: stretch; height: 2px; background: var(--brand-green); margin-top: 6px; }

  .card--front .brand-block { left: 50%; top: 60px; transform: translateX(-50%); }
  .card--front .website {
    position: absolute; left: 0; right: 0; top: 200px;
    text-align: center; color: var(--text-muted);
    font-size: 14px; letter-spacing: 1.5px;
  }

  .card--back .brand-block { left: 34px; top: 82px; width: 210px; }
  .card--back .brand__dot { width: 48px; height: 48px; border-width: 4px; }
  .card--back .brand__name { font-size: 17px; letter-spacing: .3px; }

  .card--back .divider {
    position: absolute; left: 268px; top: 70px;
    width: 1px; height: 160px; background: var(--divider);
  }
  .contact { position: absolute; left: 288px; top: 78px; color: var(--text-light); }
  .contact__name { color: var(--brand-blue); font-weight: 700; font-size: 17px; letter-spacing: .5px; }
  .contact__role { color: var(--brand-green); font-size: 13px; font-weight: 600; margin-bottom: 8px; }
  .contact__address { font-size: 13px; line-height: 1.35; margin-bottom: 4px; }
  .contact__line {
    display: flex; align-items: center; gap: 8px;
    font-size: 13px; line-height: 1.5;
  }
  .contact__icon { width: 12px; height: 12px; flex: none; }
</style>
</head>
<body>
<main class="stage">
  <section class="card card--front" aria-label="Business card front">
    <div class="brand-block">
      <span class="brand__dot"></span>
      <span class="brand__name">SUN HARBOR ENERGY</span>
      <span class="brand__rule"></span>
    </div>
    <p class="website">www.sunharborenergy.com</p>
  </section>

  <section class="card card--back" aria-label="Business card back">
    <div class="brand-block">
      <span class="brand__dot"></span>
      <span class="brand__name">SUN HARBOR ENERGY</span>
      <span class="brand__rule"></span>
    </div>
    <div class="divider"></div>
    <div class="contact">
      <p class="contact__name">DANIEL REYES</p>
      <p class="contact__role">CEO/FOUNDER</p>
      <p class="contact__address">4210 Cedar Ridge Road<br>Fairbanks, Alaska 99701</p>
      <p class="contact__line">
        <svg class="contact__icon" viewBox="0 0 12 12" aria-hidden="true"><path fill="#1f95d6" d="M2.4 1h2l1 2.6-1.3 1a6 6 0 0 0 3.3 3.3l1-1.3 2.6 1v2a1 1 0 0 1-1 1A9.5 9.5 0 0 1 1.4 2a1 1 0 0 1 1-1z"/></svg>
        555 214 7830
      </p>
      <p class="contact__line">
        <svg class="contact__icon" viewBox="0 0 12 12" aria-hidden="true"><rect x="0.5" y="2" width="11" height="8" rx="1" fill="#1f95d6"/><path d="M1 2.7 6 6.6l5-3.9" fill="none" stroke="#1c1d1f" stroke-width="1"/></svg>
        name@sunharborenergy.com
      </p>
      <p class="contact__line">
        <svg class="contact__icon" viewBox="0 0 12 12" aria-hidden="true"><circle cx="6" cy="6" r="5.5" fill="#1f95d6"/><path d="M.5 6h11M6 .5c-2 2.8-2 8.2 0 11M6 .5c2 2.8 2 8.2 0 11" fill="none" stroke="#1c1d1f" stroke-width=".9"/></svg>
        www.sunharborenergy.com
      </p>
    </div>
  </section>
</main>
</body>
</html>
```